Verdane Training Center
Golf Simulation & Character Education
Corporate
Milo Raskett
Chief Operations Officer
Brisby Center
North Charleston, SC
Milo@verdanetrainingcenter.com
verdanetrainingcenter.com
I would like for my logo design to be incorporated into the card design
logo full size of card on the back

```html
<!DOCTYPE html>
<html lang="en">
<head>
<meta charset="utf-8">
<title>Verdane Training Center – Business Card</title>
<link href="https://fonts.googleapis.com/css2?family=Open+Sans:wght@400;600;700&display=swap" rel="stylesheet">
<style>
  :root {
    --backdrop: #3a3a3a;
    --card-edge: #e4e4e4;
    --brand-red: #b3141b;
    --brand-red-dark: #7d0d12;
    --swoosh-shadow: #111111;
    --ink: #1b1b1b;
    --ink-soft: #4a4a4a;
    --icon-ink: #333333;
    --rule: #c9c9c9;
  }
  * { box-sizing: border-box; margin: 0; padding: 0; }
  html, body {
    width: 1200px;
    height: 878px;
    overflow: hidden;
    background: var(--backdrop);
    font-family: "Open Sans", Arial, sans-serif;
  }
  .card {
    position: absolute;
    left: 100px;
    top: 153px;
    width: 1000px;
    height: 572px;
    background: linear-gradient(180deg, #ffffff 0%, #f6f6f6 100%);
    border-radius: 30px;
    overflow: hidden;
    box-shadow: 0 0 0 1px var(--card-edge);
  }
  .card__swoosh {
    position: absolute;
    left: 0;
    top: 0;
    width: 1000px;
    height: 572px;
  }
  .brand {
    position: absolute;
    left: 330px;
    top: 120px;
    display: flex;
    align-items: center;
    gap: 18px;
  }
  .brand__mark {
    width: 26px;
    height: 26px;
    border-radius: 50%;
    background: var(--brand-red);
  }
  .brand__name {
    font-size: 40px;
    font-weight: 700;
    color: var(--brand-red);
    letter-spacing: 0.5px;
    line-height: 1;
  }
  .identity {
    position: absolute;
    right: 530px;
    top: 330px;
    width: 360px;
    text-align: right;
  }
  .identity__name {
    font-size: 36px;
    font-weight: 700;
    color: var(--brand-red);
    line-height: 1.1;
  }
  .identity__title {
    font-size: 21px;
    font-weight: 700;
    color: var(--ink);
    margin-top: 2px;
  }
  .identity__address {
    font-size: 21px;
    color: var(--ink-soft);
    margin-top: 14px;
    line-height: 1.3;
  }
  .divider {
    position: absolute;
    left: 494px;
    top: 318px;
    width: 1px;
    height: 180px;
    background: var(--rule);
  }
  .contact {
    position: absolute;
    left: 512px;
    top: 318px;
    list-style: none;
  }
  .contact__item {
    display: flex;
    align-items: center;
    gap: 14px;
    height: 36px;
    font-size: 20px;
    color: var(--ink);
  }
  .contact__icon {
    width: 22px;
    height: 22px;
    flex: none;
  }
</style>
</head>
<body>
  <div class="card">
    <svg class="card__swoosh" viewBox="0 0 1000 572" aria-hidden="true">
      <defs>
        <linearGradient id="swooshRed" x1="0" y1="0" x2="1" y2="1">
          <stop offset="0" stop-color="#c8181f"/>
          <stop offset="1" stop-color="#7d0d12"/>
        </linearGradient>
      </defs>
      <path d="M0 150 C 40 330, 150 490, 330 572 L0 572 Z" fill="var(--swoosh-shadow)"/>
      <path d="M0 165 C 30 340, 130 480, 300 572 L0 572 Z" fill="url(#swooshRed)"/>
    </svg>

    <div class="brand">
      <span class="brand__mark"></span>
      <span class="brand__name">Verdane Training Center</span>
    </div>

    <div class="identity">
      <p class="identity__name">Milo Raskett</p>
      <p class="identity__title">Chief Operations Officer</p>
      <p class="identity__address">Brisby Center<br>Ashbury Point,&nbsp; NC 28561</p>
    </div>

    <div class="divider"></div>

    <ul class="contact">
      <li class="contact__item">
        <svg class="contact__icon" viewBox="0 0 24 24" aria-hidden="true">
          <rect x="7" y="2" width="10" height="20" rx="2" fill="none" stroke="var(--brand-red)" stroke-width="2"/>
          <circle cx="12" cy="18" r="1.3" fill="var(--brand-red)"/>
        </svg>
        <span>843-555-0142</span>
      </li>
      <li class="contact__item">
        <svg class="contact__icon" viewBox="0 0 24 24" aria-hidden="true">
          <circle cx="12" cy="12" r="4" fill="none" stroke="var(--icon-ink)" stroke-width="2"/>
          <path d="M16 8v5a3 3 0 0 0 6 0v-1a10 10 0 1 0-4 8" fill="none" stroke="var(--icon-ink)" stroke-width="2"/>
        </svg>
        <span>Milo@verdanetrainingcenter.com</span>
      </li>
      <li class="contact__item">
        <svg class="contact__icon" viewBox="0 0 24 24" aria-hidden="true">
          <circle cx="12" cy="12" r="9" fill="none" stroke="var(--icon-ink)" stroke-width="2"/>
          <ellipse cx="12" cy="12" rx="4" ry="9" fill="none" stroke="var(--icon-ink)" stroke-width="1.5"/>
          <path d="M3 12h18" stroke="var(--icon-ink)" stroke-width="1.5"/>
        </svg>
        <span>www.verdanetrainingcenter.com</span>
      </li>
    </ul>
  </div>
</body>
</html>
```